Business Card Design

Loxley therapy is a gentle therapy where moves are made(using your hands) over muscles or joint areas create myofascial release enabling the body to rebalance itself.

Its relaxing and have heal a variety of aliments . n contrast to other hands-on modalities, where the practitioner imposes correction on the client through manipulation, Loxley Technique facilitates the body in healing itself, with minimal intervention. Because of the subtle nature of Loxley Technique, and the body's continuing response to it over several days thereafter, other forms of manipulative therapy are discouraged for up to five days after a session, as they may interfere with the efficacy of the work.

Its an energy healing work using hands.
Its relaxing but professional.
I'm think of using blues, no greens or yellows. Some wave lines .

Target Market(s)

Anybody-

Industry/Entity Type

Business

Contact Information for Business Card

Maisie's Loxley Therapy,Maisie Corbett, Loxley Therapist,Cert IV Lumacore
Kellsworth, East Reed Cove, Marrowdale, 0417 905368,Gentle therapy restoring body balance.

Requirements
Must have
• Back needs a appointment table
with this wording :
Loxley Therapy is a subtle gentle bodywork therapy where a series of moves are made over muscles that can be used to address a wide range of conditions. It is suitable for skeletal, joint and muscle problems as well as for babies and children
Date Time.

If you are unable to keep your appointment, please contact us as soon as possible.

0417905368 ozmaisie@quellmail.net
Should not have
• Dont like times new roman and handwritten script font.

```html
<!DOCTYPE html>
<html lang="en">
<head>
<meta charset="utf-8">
<title>Maisie's Loxley Therapy – Business Card</title>
<link rel="stylesheet" href="https://fonts.googleapis.com/css2?family=Questrial&display=swap">
<style>
  :root {
    --card-white: #ffffff;
    --wave-teal: #759ca2;
    --name-panel: #b3c8ca;
    --ink: #2b2b2b;
    --ink-soft: #444a4c;
  }
  html, body {
    margin: 0;
    padding: 0;
    width: 1200px;
    height: 741px;
    overflow: hidden;
    background: var(--card-white);
  }
  .card {
    position: relative;
    width: 1200px;
    height: 741px;
    overflow: hidden;
    background: var(--card-white);
    font-family: "Questrial", "Century Gothic", sans-serif;
    color: var(--ink);
  }
  .card__wave {
    position: absolute;
    inset: 0;
    width: 1200px;
    height: 741px;
  }
  .card__wave-fill { fill: var(--wave-teal); }
  .card__wave-line { fill: none; stroke: var(--card-white); stroke-width: 4; }

  .brand {
    position: absolute;
    left: 174px;
    top: 40px;
    margin: 0;
    font-weight: 400;
    font-size: 87px;
    line-height: 1;
    letter-spacing: 1px;
    white-space: nowrap;
  }
  .tagline {
    position: absolute;
    left: 296px;
    top: 124px;
    margin: 0;
    font-size: 36px;
    line-height: 1;
    letter-spacing: 0.5px;
    white-space: nowrap;
  }
  .name-panel {
    position: absolute;
    left: 560px;
    top: 285px;
    width: 461px;
    height: 117px;
    background: var(--name-panel);
    text-align: center;
  }
  .name-panel__name {
    margin: 14px 0 0;
    font-size: 50px;
    line-height: 1;
    white-space: nowrap;
  }
  .name-panel__surname { color: var(--ink-soft); }
  .name-panel__role {
    margin: 8px 0 0;
    font-size: 29px;
    line-height: 1;
    letter-spacing: 0.5px;
    white-space: nowrap;
  }
  .contact {
    position: absolute;
    left: 43px;
    top: 437px;
    margin: 0;
    padding: 0;
    list-style: none;
    font-size: 38px;
    line-height: 1;
    letter-spacing: 0.5px;
  }
  .contact__item { white-space: nowrap; }
  .contact__item--phone { margin-bottom: 24px; }
  .contact__item--email { margin-bottom: 24px; }
  .contact__item--place { margin-bottom: 10px; }
</style>
</head>
<body>
<main class="card">
  <svg class="card__wave" viewBox="0 0 1200 741" aria-hidden="true">
    <path class="card__wave-fill" d="M30 0 C 210 340, 620 575, 1200 728 L1200 0 Z"/>
    <path class="card__wave-line" d="M50 0 C 225 325, 625 548, 1200 702"/>
  </svg>

  <h1 class="brand">Maisie's Loxley Therapy</h1>
  <p class="tagline">Gentle therapy restoring body balance.</p>

  <section class="name-panel">
    <p class="name-panel__name">Maisie <span class="name-panel__surname">Corbett</span></p>
    <p class="name-panel__role">Loxley Therapist, Cert IV</p>
  </section>

  <ul class="contact">
    <li class="contact__item contact__item--phone">0417905368</li>
    <li class="contact__item contact__item--email">ozmaisie@quellmail.net</li>
    <li class="contact__item contact__item--place">Lumacore Kellsworth</li>
    <li class="contact__item contact__item--place">East Reed Cove</li>
    <li class="contact__item">Marrowdale</li>
  </ul>
</main>
</body>
</html>
```